Wander the Quiet Logo/Business Card

Project MUST include a logo with business card. See attached picture.

Logo is attached to brief but I'd like to add the tagline: "What you don't know that you don't know" Logo should also have an emblem that represents the Orbiton movie concept of red pill or blue pill (one in each hand). This emblem can be used with WanDer the QuIet or without.

Two sided card

Back can have the question mark logo that is attached

I'd like the background to be black.

On side have person's info:
Tobias Ferrell
Trainer, Speaker, Author
p: 555-014-2287
e: t@wanderthequiet.example
www.wanderthequiet.example

Have find us on chatterly, pipwave (just logos)

Target Market(s)

People looking to know what they don't know, self development, personal growth

Industry/Entity Type

Movie

Requirements
Must have
• qr code
two sided

```html
<!DOCTYPE html>
<html lang="en">
<head>
<meta charset="utf-8">
<title>Wander the Quiet — Business Card</title>
<link rel="stylesheet" href="https://fonts.googleapis.com/css2?family=Oswald:wght@600&family=Arimo:wght@400&display=swap">
<style>
  :root {
    --page: #ffffff;
    --card: #000000;
    --ink: #ffffff;
    --accent: #f7941d;
    --mark: #1e6aa8;
  }
  html, body {
    margin: 0;
    width: 1200px;
    height: 1200px;
    overflow: hidden;
    background: var(--page);
  }
  .canvas {
    position: relative;
    width: 1200px;
    height: 1200px;
  }
  .card {
    position: absolute;
    top: 455px;
    width: 480px;
    height: 290px;
    background: var(--card);
    color: var(--ink);
    font-family: "Arimo", Arial, sans-serif;
  }
  .card--front { left: 100px; }
  .card--back  { left: 620px; }

  /* front */
  .brand {
    position: absolute;
    left: 38px;
    top: 96px;
    display: flex;
    align-items: center;
    gap: 26px;
  }
  .brand-dot {
    width: 62px;
    height: 62px;
    border-radius: 50%;
    background: var(--mark);
    flex: none;
  }
  .brand-name {
    font-family: "Oswald", "Arial Narrow", sans-serif;
    font-weight: 600;
    font-size: 44px;
    line-height: 44px;
    letter-spacing: 0.5px;
    color: var(--ink);
    text-transform: uppercase;
  }
  .tagline {
    position: absolute;
    left: 150px;
    top: 194px;
    font-size: 7.5px;
    letter-spacing: 0.3px;
    text-transform: uppercase;
  }
  .front-phone {
    position: absolute;
    left: 0;
    right: 0;
    top: 232px;
    padding-left: 60px;
    text-align: center;
    font-size: 15px;
    letter-spacing: 0.5px;
  }

  /* back */
  .back-dot {
    position: absolute;
    left: 34px;
    top: 52px;
    width: 36px;
    height: 36px;
    border-radius: 50%;
    background: var(--mark);
  }
  .person {
    position: absolute;
    left: 30px;
    top: 116px;
    font-size: 13px;
    line-height: 16px;
  }
  .person-name { text-transform: uppercase; }
  .person-role { color: var(--accent); }
  .contact {
    position: absolute;
    left: 26px;
    top: 168px;
    font-size: 13px;
    line-height: 15px;
    letter-spacing: 0.5px;
    text-transform: uppercase;
  }
</style>
</head>
<body>
  <main class="canvas">
    <section class="card card--front" aria-label="Card front">
      <div class="brand">
        <span class="brand-dot"></span>
        <div class="brand-name">Wander the<br>Quiet</div>
      </div>
      <p class="tagline" style="margin:0">What you don't know that you don't know</p>
      <p class="front-phone" style="margin:0">555 - 014 - 3390</p>
    </section>

    <section class="card card--back" aria-label="Card back">
      <span class="back-dot"></span>
      <div class="person">
        <div class="person-name">Tobias Ferrell</div>
        <div class="person-role">Trainer . Speaker . Author</div>
      </div>
      <div class="contact">
        <div>555 - 014 - 2287</div>
        <div>t@wanderthequiet.example</div>
        <div>www.wanderthequiet.example</div>
      </div>
    </section>
  </main>
</body>
</html>
```